website design for a new age Real Estate Security Business

We are launching a business in real estate which no body else is doing. We are going to use technology in terms of software and hardware to provide our services.

We are going to use Big Data, IOT etc.. for our services.

NOTE: We don't want to see Shiel or buildings etc.. that directly suggests Real estate or security on this design

Target Market(s)

India

Industry/Entity Type

Real Estate

Number of Pages Required

4 page

Font styles to use
Sans Serif
Other font styles liked:
• Use Google Fonts

Requirements
Must have
• Home Page should be trendy and colourful should give user confidence to subscribe to our service.
Nice to have
• Use Google fonts.
Should not have
• Design shouldnt have Shield or Buildings that directly suggests real estate or security.

```html
<!DOCTYPE html>
<html lang="en">
<head>
<meta charset="utf-8">
<title>Parcel Sentry</title>
<link rel="stylesheet" href="https://fonts.googleapis.com/css2?family=Oswald:wght@400;500&family=Roboto+Condensed:wght@400;700&family=Open+Sans:ital,wght@0,400;0,600;1,400&display=swap">
<style>
:root{
  --navy:#050d1a;
  --teal:#1ea5b8;
  --teal-dark:#168b9c;
  --orange:#f26b1d;
  --ink:#2b2b2b;
  --body:#555;
  --grey-bg:#eceeef;
  --green:#8cc63f;
  --footer:#1b1b1b;
  --white:#fff;
  --yellow:#f4a614;
}
*{box-sizing:border-box;margin:0;padding:0}
html,body{width:1200px;height:2466px;overflow:hidden}
body{position:relative;background:var(--white);font-family:"Open Sans",sans-serif;color:var(--body)}
.abs{position:absolute}

/* hero */
.hero{position:absolute;left:0;top:0;width:1200px;height:720px}
.hero-art{position:absolute;inset:0}
.topbar{position:absolute;left:0;top:0;width:1200px;height:95px;border-bottom:1px solid rgba(255,255,255,.25)}
.brand{position:absolute;left:100px;top:30px;display:flex;align-items:center;gap:10px;font-family:"Oswald",sans-serif;font-weight:500;font-size:27px;color:var(--white);letter-spacing:.5px}
.brand-dot{width:22px;height:22px;border-radius:50%;background:var(--white)}
.nav{position:absolute;right:100px;top:38px;display:flex;gap:44px;font-family:"Roboto Condensed",sans-serif;font-weight:700;font-size:16px;color:var(--white);letter-spacing:.4px}
.nav .active{color:var(--orange)}
.hero-tag{position:absolute;left:0;width:1200px;top:424px;text-align:center;font-family:"Oswald",sans-serif;font-size:24px;color:var(--white)}
.btn-learn{position:absolute;left:527px;top:480px;width:143px;height:38px;background:var(--orange);color:var(--white);font-family:"Oswald",sans-serif;font-size:17px;text-align:center;line-height:38px}
.node-label{position:absolute;width:140px;text-align:center;font-family:"Oswald",sans-serif;font-size:22px;color:var(--white)}

/* welcome */
.welcome-title{position:absolute;left:0;width:1200px;top:768px;text-align:center;font-family:"Roboto Condensed",sans-serif;font-weight:700;font-size:34px;color:var(--ink)}
.welcome-text{position:absolute;left:165px;width:870px;top:826px;text-align:center;font-size:11.5px;line-height:20px;color:var(--body)}

/* features */
.feature h3{position:absolute;font-family:"Roboto Condensed",sans-serif;font-weight:400;font-size:24px;color:var(--ink)}
.feature p{position:absolute;width:530px;font-size:11.5px;line-height:24px;color:var(--body)}
.btn-read{position:absolute;width:96px;height:35px;border-radius:18px;background:var(--teal);color:var(--white);font-family:"Roboto Condensed",sans-serif;font-size:13px;text-align:center;line-height:35px}
.feature-art{position:absolute;border-radius:50%}

/* testimonials */
.testimonials{position:absolute;left:0;top:1607px;width:1200px;height:401px;background:linear-gradient(180deg,#eef0f1,#e4e6e7)}
.testimonials h2{position:absolute;left:0;width:1200px;top:78px;text-align:center;font-family:"Roboto Condensed",sans-serif;font-weight:400;font-size:30px;color:var(--ink)}
.t-rule{position:absolute;left:570px;top:132px;width:62px;height:3px;background:var(--teal)}
.avatar{position:absolute;width:120px;height:120px;border-radius:50%;border:2px solid #9fd7df;background:radial-gradient(circle at 50% 40%,#d9a98a,#8a6752 70%,#5b4538)}
.quote{position:absolute;width:330px;font-style:italic;font-size:12px;line-height:21px;color:#444}
.t-name{position:absolute;font-family:"Roboto Condensed",sans-serif;font-size:14px;color:var(--ink)}
.stars{position:absolute;font-size:15px;letter-spacing:1px;color:var(--teal)}
.stars span{color:#333}

/* subscribe band */
.subscribe{position:absolute;left:0;top:2008px;width:1200px;height:102px;background:var(--green)}
.sub-text{position:absolute;left:242px;top:30px;font-family:"Roboto Condensed",sans-serif;font-size:16px;line-height:23px;color:var(--white)}
.sub-input{position:absolute;left:560px;top:32px;width:380px;height:41px;border-radius:21px 0 0 21px;background:var(--white);font-size:12px;color:#666;padding-left:24px;line-height:41px}
.sub-btn{position:absolute;left:932px;top:32px;width:126px;height:41px;border-radius:0 21px 21px 0;background:#3a3a3a;color:var(--white);font-family:"Roboto Condensed",sans-serif;font-size:14px;text-align:center;line-height:41px}

/* footer */
.footer{position:absolute;left:0;top:2110px;width:1200px;height:356px;background:var(--footer);color:var(--white)}
.footer h4{position:absolute;top:52px;font-family:"Roboto Condensed",sans-serif;font-weight:400;font-size:18px}
.f-row{position:absolute;left:100px;display:flex;gap:14px;font-size:12.5px;line-height:20px}
.f-row svg{flex:none}
.f-note{position:absolute;left:428px;top:96px;width:300px;font-size:11.5px;line-height:20px}
.f-field{position:absolute;left:428px;top:148px;width:286px;height:42px;background:var(--white);color:#666;font-size:11.5px;line-height:42px;padding-left:12px}
.f-btn{position:absolute;left:428px;top:205px;width:114px;height:40px;background:var(--teal);font-family:"Roboto Condensed",sans-serif;font-size:14px;text-align:center;line-height:40px}
.links{position:absolute;left:810px;top:98px;list-style:none;font-size:12px;line-height:24px}
.social{position:absolute;left:1003px;top:96px;list-style:none;font-size:14px}
.social li{display:flex;align-items:center;gap:10px;height:37px}
.social i{width:26px;height:26px;border-radius:50%;border:1.5px solid var(--white)}
.copyright{position:absolute;left:0;width:1200px;top:2428px;text-align:center;font-size:12px;color:var(--white)}
</style>
</head>
<body>

<header class="hero">
  <svg class="hero-art" width="1200" height="720" viewBox="0 0 1200 720">
    <defs>
      <radialGradient id="glow" cx="50%" cy="45%" r="60%">
        <stop offset="0" stop-color="#1b5fa8"/>
        <stop offset=".45" stop-color="#0b2a52"/>
        <stop offset="1" stop-color="#040b17"/>
      </radialGradient>
    </defs>
    <path d="M0 0H1200V645L600 715L0 645Z" fill="var(--navy)"/>
    <path d="M0 0H1200V645L600 715L0 645Z" fill="url(#glow)" role="img" aria-label="Glowing blue data landscape of points and lines"/>
    <path d="M0 645L600 715L1200 645" fill="none" stroke="var(--teal)" stroke-width="4"/>
    <!-- slider arrows -->
    <path d="M68 368L42 392L68 416" fill="none" stroke="#cfd8e3" stroke-width="2"/>
    <path d="M1132 368L1158 392L1132 416" fill="none" stroke="#cfd8e3" stroke-width="2"/>
    <!-- process cycle -->
    <ellipse cx="600" cy="455" rx="190" ry="115" fill="none" stroke="#fff" stroke-width="4" stroke-dasharray="16 11"/>
    <circle cx="360" cy="445" r="72" fill="var(--teal)" stroke="rgba(30,165,184,.4)" stroke-width="8"/>
    <circle cx="600" cy="330" r="72" fill="var(--orange)" stroke="rgba(242,107,29,.4)" stroke-width="8"/>
    <circle cx="840" cy="445" r="72" fill="var(--teal)" stroke="rgba(30,165,184,.4)" stroke-width="8"/>
    <!-- database icon -->
    <g fill="#fff">
      <ellipse cx="360" cy="395" rx="17" ry="6"/>
      <rect x="343" y="401" width="34" height="9" rx="4"/>
      <rect x="343" y="413" width="34" height="9" rx="4"/>
      <rect x="343" y="425" width="34" height="9" rx="4"/>
    </g>
    <!-- chart icon -->
    <g fill="#fff">
      <rect x="582" y="290" width="5" height="28"/>
      <rect x="591" y="300" width="5" height="18"/>
      <rect x="600" y="295" width="5" height="23"/>
      <circle cx="612" cy="296" r="8" fill="none" stroke="#fff" stroke-width="3"/>
      <rect x="578" y="318" width="44" height="3"/>
    </g>
    <!-- send icon -->
    <path d="M822 405L862 385L850 428L840 414L832 424L832 410Z" fill="#fff"/>
  </svg>

  <div class="topbar">
    <div class="brand"><span>PARCEL SENTRY</span><span class="brand-dot"></span></div>
    <nav class="nav"><span class="active">HOME</span><span>SERVICES</span><span>CONTACT US</span><span>PRICING</span></nav>
  </div>

  <div class="node-label" style="left:290px;top:437px">DATA</div>
  <div class="node-label" style="left:530px;top:337px">ANALYSIS</div>
  <div class="node-label" style="left:770px;top:433px">ACTION</div>
  <div class="hero-tag">TO KEEP YOUR PROPERTY SAFE</div>
  <div class="btn-learn">LEARN MORE</div>
</header>

<section class="welcome">
  <h1 class="welcome-title">WELCOME TO PARCEL SENTRY</h1>
  <p class="welcome-text">Sed ut perspiciatis unde omnis iste natus error sit voluptatem accusantium doloremque laudantium, totam rem aperiam, eaque ipsa quae ab illo inventore veritatis et quasi architecto beatae vitae dicta sunt explicabo. Nemo enim ipsam voluptatem quia voluptas sit aspernatur aut odit aut fugit, sed quia consequuntur magni dolores eos qui ratione voluptatem sequi nesciunt. Neque porro quisquam est, qui dolorem ipsum quia dolor sit amet, consectetur, adipisci velit</p>
  <svg class="abs" style="left:485px;top:922px" width="230" height="30" viewBox="0 0 230 30">
    <line x1="0" y1="15" x2="95" y2="15" stroke="var(--teal)" stroke-width="1.5"/>
    <line x1="135" y1="15" x2="230" y2="15" stroke="var(--teal)" stroke-width="1.5"/>
    <circle cx="115" cy="15" r="10" fill="none" stroke="#2b3a4a" stroke-width="2.5"/>
  </svg>
</section>

<section class="feature">
  <svg class="abs" style="left:166px;top:993px" width="244" height="244" viewBox="0 0 244 244">
    <circle cx="122" cy="122" r="119" fill="none" stroke="#666" stroke-width="1.5" stroke-dasharray="1 5"/>
    <circle cx="122" cy="122" r="110" fill="var(--teal)" role="img" aria-label="Illustration of a locked document folder"/>
  </svg>
  <h3 style="left:498px;top:1030px">DOC SECURE</h3>
  <p style="left:498px;top:1072px">Sed ut perspiciatis unde omnis iste natus error sit voluptatem accusantium doloremque laudantium, totam rem aperiam, eaque ipsa quae ab illo inventore veritatis et quasi architecto beatae vitae dicta sunt explicabo. Nemo enim ipsam voluptatem quia voluptas sit aspernatur aut odit aut fugit, sed quia consequuntur magni dolores eos qui ratione voluptatem sequi nesciunt.</p>
  <div class="btn-read" style="left:498px;top:1193px">READ MORE</div>
</section>

<section class="feature">
  <h3 style="left:165px;top:1313px">LAND SECURE</h3>
  <p style="left:165px;top:1355px">Sed ut perspiciatis unde omnis iste natus error sit voluptatem accusantium doloremque laudantium, totam rem aperiam, eaque ipsa quae ab illo inventore veritatis et quasi architecto beatae vitae dicta sunt explicabo. Nemo enim ipsam voluptatem quia voluptas sit aspernatur aut odit aut fugit, sed quia consequuntur magni dolores eos qui ratione voluptatem sequi nesciunt.</p>
  <div class="btn-read" style="left:165px;top:1476px">READ MORE</div>
  <svg class="abs" style="left:783px;top:1278px" width="244" height="244" viewBox="0 0 244 244">
    <circle cx="122" cy="122" r="119" fill="none" stroke="#666" stroke-width="1.5" stroke-dasharray="1 5"/>
    <circle cx="122" cy="122" r="110" fill="var(--yellow)" role="img" aria-label="Illustration of a protected home emblem"/>
  </svg>
</section>

<section class="testimonials" role="img" aria-label="Soft faded interior room backdrop">
  <h2>TESTIMONIALS</h2>
  <div class="t-rule"></div>

  <div class="avatar" role="img" aria-label="Portrait of client" style="left:98px;top:142px"></div>
  <p class="quote" style="left:240px;top:188px">" Nemo enim ipsam voluptatem quia voluptas sit aspernatur aut odit aut fugit, sed quia consequuntur magni dolores eos qui ratione voluptatem sequi nesciunt.</p>
  <div class="t-name" style="left:240px;top:267px">DARA VENN - PARCEL SENTRY</div>
  <div class="stars" style="left:240px;top:298px">★★★★<span>★</span></div>

  <div class="avatar" role="img" aria-label="Portrait of client" style="left:636px;top:142px"></div>
  <p class="quote" style="left:778px;top:188px">" Nemo enim ipsam voluptatem quia voluptas sit aspernatur aut odit aut fugit, sed quia consequuntur magni dolores eos qui ratione voluptatem sequi nesciunt.</p>
  <div class="t-name" style="left:778px;top:267px">DARA VENN - PARCEL SENTRY</div>
  <div class="stars" style="left:778px;top:298px">★★★★<span>★</span></div>
</section>

<section class="subscribe">
  <svg class="abs" style="left:186px;top:36px" width="40" height="34" viewBox="0 0 40 34">
    <path d="M2 16L38 2L30 32L19 22L14 30L14 19L38 2" fill="none" stroke="#fff" stroke-width="2.5" stroke-linejoin="round"/>
  </svg>
  <div class="sub-text">SUBSCRIBE TO RECEIVE UPDATES AND<br>EXCLUSIVE OFFERS.</div>
  <div class="sub-input">Enter your E - mail</div>
  <div class="sub-btn">SUBSCRIBE</div>
</section>

<footer class="footer">
  <h4 style="left:100px">CONTACT US</h4>
  <div class="f-row" style="top:100px">
    <svg width="16" height="22" viewBox="0 0 16 22"><path d="M8 1C4 1 1 4 1 8c0 5 7 13 7 13s7-8 7-13c0-4-3-7-7-7z" fill="none" stroke="#fff" stroke-width="1.6"/><circle cx="8" cy="8" r="2.5" fill="none" stroke="#fff" stroke-width="1.6"/></svg>
    <span>Parcel Sentry<br>Elmbridge, Larkfield, Kent,</span>
  </div>
  <div class="f-row" style="top:158px">
    <svg width="18" height="18" viewBox="0 0 18 18"><path d="M3 1l4 4-2 2c1 3 3 5 6 6l2-2 4 4-3 2C7 17 1 11 1 4z" fill="none" stroke="#fff" stroke-width="1.4"/></svg>
    <span>Phone :&nbsp; +44(0)20 5550 0142</span>
  </div>
  <div class="f-row" style="top:194px">
    <svg width="18" height="14" viewBox="0 0 18 14"><rect x="1" y="1" width="16" height="12" fill="none" stroke="#fff" stroke-width="1.4"/><path d="M1 1l8 7 8-7" fill="none" stroke="#fff" stroke-width="1.4"/></svg>
    <span>Email: info@parcelsentry.example</span>
  </div>

  <h4 style="left:428px">SIGN UP TO RECEIVE EMAIL</h4>
  <p class="f-note">Excepteur sint occaecat cupidatat non proident, sunt in culpa qui Nemo enim ipsam voluptatem</p>
  <div class="f-field">Enter Name</div>
  <div class="f-btn">SUBSCRIBE</div>

  <h4 style="left:810px">QUICK LINKS</h4>
  <ul class="links"><li>Home</li><li>About Us</li><li>Services</li><li>Pricing</li><li>Blog</li><li>Contact Us</li></ul>

  <h4 style="left:1003px">SOCIAL</h4>
  <ul class="social">
    <li><i></i>Feedbook</li>
    <li><i></i>Chirper</li>
    <li><i></i>Circles+</li>
    <li><i></i>Viewtube</li>
  </ul>
</footer>
<div class="copyright">Copyright © Parcel Sentry 2017. All rights reserved.</div>

</body>
</html>
```